Overview of Elder Abuse Resources Brochure

We need a 2-page brochure that provides a list of resources for elders in tribal communities in the US and those who care for them. We want it to be simple and easy to read, and easy to see the difference between each resource. We would also like eye-catching images or graphics. Please keep the images on the front, and add any photos or graphics that depict Native American elders. We need both of our logos on the first page, in the far-right column. Please refer to the attached image for our brand colors and a font suggestion. Please keep the three columns on each page, but delete the blank pages in the document.

```html
<!DOCTYPE html>
<html lang="en">
<head>
<meta charset="utf-8">
<title>Services for Elders &amp; People Who Care for Them</title>
<link rel="stylesheet" href="https://fonts.googleapis.com/css2?family=Roboto+Condensed:wght@700&family=Roboto:ital,wght@0,400;0,500;0,700;1,400;1,500&display=swap">
<style>
:root{
  --backdrop:#8a8a8a;
  --teal:#72a8b0;
  --teal-dark:#5f9aa3;
  --rust:#9e5a52;
  --gold:#e0b05a;
  --ink:#2b2b2b;
  --white:#ffffff;
  --pale:#f4f7f8;
  --blush:#f1e2e2;
  --mist:#e3ecee;
  --rule:#c79a96;
}
*{box-sizing:border-box;margin:0;padding:0}
html,body{width:900px;height:1200px;overflow:hidden;background:var(--backdrop)}
body{position:relative;font-family:"Roboto",Arial,sans-serif;color:var(--ink)}
.page{position:absolute;left:120px;width:660px;height:510px;display:flex;overflow:hidden}
.page--outside{top:79px}
.page--inside{top:611px}
.panel{position:relative;width:220px;height:510px;overflow:hidden;flex:none}
.cond{font-family:"Roboto Condensed","Arial Narrow",sans-serif;font-weight:700;text-transform:uppercase}
.photo{position:absolute}
.brand{font-family:"Roboto Condensed","Arial Narrow",sans-serif;font-weight:700;font-size:8px;line-height:1.1;text-transform:uppercase;display:flex;align-items:center;gap:4px;white-space:nowrap}
.brand i{display:inline-block;width:10px;height:10px;border-radius:50%;flex:none}

/* Outside panel 1 */
.respect{background:var(--teal);color:var(--white)}
.respect__photos{position:absolute;top:0;left:0;width:220px;height:95px}
.respect__body{position:absolute;top:95px;left:0;right:0;padding:12px 22px 0 21px}
.respect h2{font-size:13.5px;margin-bottom:6px}
.respect p{font-size:9.2px;line-height:11px;margin-bottom:11px}
.respect h3{font-size:10px;margin:20px 0 6px}
.contact{display:flex;gap:6px;padding:4px 0;border-bottom:1px dotted rgba(255,255,255,.7);font-size:8.9px;line-height:10.9px;margin-right:-10px}
.contact:last-child{border-bottom:none}
.contact svg{flex:none;margin-top:1px}
.contact b{font-weight:700}
.contact em{display:block;padding-left:8px}

/* Outside panel 2 */
.mailer{background:var(--pale)}
.mailer__line{position:absolute;top:158px;left:97px;width:123px;border-top:1px solid #9bb8bd}
.mailer__to{position:absolute;top:170px;left:96px;writing-mode:vertical-rl;transform:rotate(180deg);font-size:10px;color:var(--teal-dark);font-weight:700}
.mailer__brands{position:absolute;left:10px;bottom:18px;height:104px;writing-mode:vertical-rl;transform:rotate(180deg);display:flex;gap:6px}
.mailer__brands .brand:first-child{color:var(--teal-dark)}
.mailer__brands .brand:last-child{color:var(--gold)}
.mailer__brands .brand{white-space:normal}
.return{position:absolute;left:138px;bottom:17px;height:102px;writing-mode:vertical-rl;transform:rotate(180deg);font-size:8px;line-height:11px}
.return strong{font-family:"Roboto Condensed","Arial Narrow",sans-serif;text-transform:uppercase}

/* Outside panel 3 */
.cover{background:var(--white)}
.cover__brands{position:absolute;top:12px;right:8px;display:flex;gap:8px}
.cover__brands .brand:first-child{color:var(--gold)}
.cover__brands .brand:last-child{color:var(--rust)}
.cover__title{position:absolute;top:61px;left:17px;font-size:26px;line-height:21.7px;white-space:nowrap}
.cover__title span{display:block}
.t-dark{color:var(--ink)}.t-rust{color:var(--rust)}.t-teal{color:var(--teal)}
.cover__photo{top:158px;left:0;width:220px;height:240px}
.cover__wave{position:absolute;top:370px;left:0}
.cover__band{position:absolute;top:390px;left:0;right:0;bottom:0;background:var(--rust);color:var(--white);padding:16px 10px 0 10px}
.ask{display:flex;align-items:center;gap:10px;font-size:9.5px;line-height:10.8px;padding:4px 0 5px 31px;border-bottom:1px dotted rgba(255,255,255,.6);margin:0 20px 0 0}
.ask:nth-child(2){border-bottom:1px dotted rgba(255,255,255,.6)}
.cover__band p.lead{font-weight:700;font-size:11.6px;line-height:12.8px;text-align:center;margin-top:5px}

/* Inside panel 1 */
.stories{background:var(--white)}
.stories__brands{position:absolute;top:16px;left:12px;display:flex;gap:10px}
.stories__brands .brand:first-child{color:var(--teal-dark)}
.stories__brands .brand:last-child{color:var(--gold)}
.stories h2{position:absolute;top:80px;left:23px;font-size:14px;line-height:15px;font-weight:500}
.stories ul{position:absolute;top:123px;left:23px;right:16px;list-style:none}
.stories li{position:relative;padding-left:14px;font-size:9.2px;line-height:11px;margin-bottom:5.5px}
.stories li::before{content:"";position:absolute;left:1px;top:4px;width:4px;height:4px;border-radius:50%;background:var(--ink)}
.stories__photo{top:300px;left:0;width:260px;height:210px}

/* Inside panels 2 & 3 */
.resources__head{height:96px;display:flex;align-items:center;padding-left:8px;color:var(--white)}
.resources__figure{width:74px;height:76px;border-radius:4px;flex:none}
.resources__title{margin-left:12px;margin-top:22px;white-space:nowrap}
.resources__title small{display:block;font-size:11px;line-height:12px}
.resources__title big{display:block;font-size:29px;line-height:29px}
.elders{background:var(--blush)}
.elders .resources__head{background:var(--rust)}
.elders .resources__figure{background:rgba(255,255,255,.85)}
.carers{background:var(--mist)}
.carers .resources__head{background:var(--teal);padding-left:14px}
.carers .resources__figure{width:24px;background:rgba(255,255,255,.85)}
.carers .resources__title{margin-left:8px}
.list{padding:20px 12px 0 14px}
.item{display:flex;gap:10px;padding:0 0 6px;margin-bottom:5px;border-bottom:1px dotted var(--rule);font-size:7.9px;line-height:9.8px}
.item:last-child{border-bottom:none}
.item svg{flex:none;margin-top:1px}
.item h4{font-size:8.6px;line-height:10px;font-weight:500;text-transform:uppercase;margin-bottom:1px}
.item em{font-style:italic}
.elders .item h4{color:var(--rust)}
.carers .item h4{color:var(--teal-dark)}
.carers .item{border-bottom-color:#8fb6bc}
.carers .sub{font-style:italic;font-weight:500;font-size:9.6px;text-align:center;padding-top:4px}
.carers .list{padding-top:12px}
.kin{background:var(--teal);color:var(--white);text-align:center;padding:9px 0 8px;margin:0 0 12px}
.kin strong{display:block;font-style:italic;font-weight:500;font-size:9.6px}
.kin span{font-size:8px;line-height:10px;display:block}
.waves{position:absolute;left:0;bottom:0}
.url{word-break:break-all}
</style>
</head>
<body>

<section class="page page--outside">
  <div class="panel respect">
    <div class="respect__photos">
      <div class="photo" style="left:0;top:0;width:105px;height:95px;background:linear-gradient(135deg,#b5b0aa,#6f6962)" role="img" aria-label="Portrait of an older Native American man with long grey hair"></div>
      <div class="photo" style="left:105px;top:0;width:115px;height:95px;background:linear-gradient(135deg,#7a2a2a,#b0463c 55%,#2f6a4a)" role="img" aria-label="Older Native American woman wrapped in a red patterned blanket"></div>
    </div>
    <div class="respect__body">
      <h2 class="cond">Respect for Elders</h2>
      <p>Do you have concerns about an Elder, maybe you see that they are not taking care of themselves, or family only comes once a month when the Elder has money?</p>
      <p>Is an Elder telling you that they are not treated with respect or that someone is bothering them?</p>
      <p>These may be signs of Elder abuse, neglect or exploitation.</p>
      <h3 class="cond">For help contact:</h3>
      <div class="contact">
        <svg width="18" height="18" viewBox="0 0 18 18"><circle cx="9" cy="9" r="8" fill="none" stroke="#fff" stroke-width="1.2"/><circle cx="6.5" cy="7" r="1.6" fill="none" stroke="#fff"/><circle cx="11.5" cy="7" r="1.6" fill="none" stroke="#fff"/><path d="M4 12.5a2.5 2.5 0 0 1 5 0M9 12.5a2.5 2.5 0 0 1 5 0" fill="none" stroke="#fff"/></svg>
        <div><b>Your Tribal Social Services or Elders Department:</b><em>insert contact information for your tribal services, law enforcement, etc.</em></div>
      </div>
      <div class="contact">
        <svg width="18" height="18" viewBox="0 0 18 18"><circle cx="9" cy="9" r="8" fill="none" stroke="#fff" stroke-width="1.2"/><circle cx="9" cy="9" r="4.5" fill="none" stroke="#fff"/><path d="M4.5 9h9M9 4.5v9" stroke="#fff"/></svg>
        <div><b>The Elder Care Finder for information on Adult Protective Services</b><br>1-800-555-0116</div>
      </div>
      <div class="contact" style="align-items:center">
        <svg width="18" height="18" viewBox="0 0 18 18"><circle cx="9" cy="9" r="8" fill="#fff"/><circle cx="9" cy="9" r="6.5" fill="#b23b34"/><path d="M9 5v5" stroke="#fff" stroke-width="1.6"/><circle cx="9" cy="12.4" r=".9" fill="#fff"/></svg>
        <div>If a serious emergency, call 911.</div>
      </div>
      <div class="contact">
        <svg width="18" height="18" viewBox="0 0 18 18"><circle cx="9" cy="9" r="8" fill="none" stroke="#fff" stroke-width="1.2"/><path d="M9 13s-4-2.4-4-5a2 2 0 0 1 4-.6A2 2 0 0 1 13 8c0 2.6-4 5-4 5z" fill="#fff"/></svg>
        <div>For mental health support for yourself or an Elder, call or text 1-800-555-0988</div>
      </div>
      <div class="contact">
        <svg width="18" height="18" viewBox="0 0 18 18"><circle cx="9" cy="9" r="8" fill="#fff"/><circle cx="9" cy="9" r="6.5" fill="#a6524a"/><path d="M6.3 5.5l1.5-.4.9 2-1 .8a5 5 0 0 0 2.4 2.4l.8-1 2 .9-.4 1.5c-3.5.3-6.5-2.7-6.2-6.2z" fill="#fff"/></svg>
        <div><b>Family Safety Hotline</b><br>1.800.555.0172</div>
      </div>
    </div>
  </div>

  <div class="panel mailer">
    <div class="mailer__line"></div>
    <div class="mailer__to">TO</div>
    <div class="mailer__brands">
      <div class="brand"><i style="background:var(--teal)"></i>Council for Native Elder Wellbeing</div>
      <div class="brand"><i style="background:var(--gold)"></i>Tribal Elder Safety Network</div>
    </div>
    <div class="return">
      <strong>Council for Native Elder Wellbeing</strong><br>
      240 Cedar Ridge Rd #12<br>Fairhaven, MD 20000<br>(301) 555-0148<br>nativeelders.example
    </div>
  </div>

  <div class="panel cover">
    <div class="cover__brands">
      <div class="brand"><i style="background:var(--gold)"></i>Tribal Elder<br>Safety Network</div>
      <div class="brand"><i style="background:var(--teal)"></i>Council for Native<br>Elder Wellbeing</div>
    </div>
    <h1 class="cover__title cond">
      <span class="t-dark">Services</span>
      <span class="t-rust">For Elders &amp;</span>
      <span class="t-teal">People who</span>
      <span class="t-teal">care for them</span>
    </h1>
    <div class="photo cover__photo" style="background:linear-gradient(160deg,#b49a82,#d8c3ad 45%,#b23c82 90%)" role="img" aria-label="Smiling older Native American woman in a pink shirt and turquoise necklace"></div>
    <svg class="cover__wave" width="220" height="40" viewBox="0 0 220 40"><path d="M0 26 C60 6 140 12 220 0 V40 H0z" fill="var(--gold)"/><path d="M0 36 C70 16 140 24 220 10 V40 H0z" fill="var(--rust)"/></svg>
    <div class="cover__band">
      <div>
        <div class="ask">
          <svg width="20" height="20" viewBox="0 0 20 20"><circle cx="10" cy="10" r="9" fill="#fff"/><path d="M10 13.5s-4-2.3-4-5a2 2 0 0 1 4-.6 2 2 0 0 1 4 .6c0 2.7-4 5-4 5z" fill="var(--rust)"/></svg>
          <span>Are you caring for an Elder<br>or a Grandchild?</span>
        </div>
        <div class="ask">
          <svg width="20" height="20" viewBox="0 0 20 20"><circle cx="10" cy="10" r="9" fill="#fff"/><circle cx="7.5" cy="8" r="1.8" fill="none" stroke="var(--rust)"/><circle cx="12.5" cy="8" r="1.8" fill="none" stroke="var(--rust)"/><path d="M4.8 14a2.7 2.7 0 0 1 5.4 0M9.8 14a2.7 2.7 0 0 1 5.4 0" fill="none" stroke="var(--rust)"/></svg>
          <span>Are you an Elder who needs<br>help staying at home?</span>
        </div>
      </div>
      <p class="lead">These programs and information<br>can be a helpful resource.</p>
    </div>
  </div>
</section>

<section class="page page--inside">
  <div class="panel stories">
    <div class="stories__brands">
      <div class="brand"><i style="background:var(--teal)"></i>Council for Native<br>Elder Wellbeing</div>
      <div class="brand"><i style="background:var(--gold)"></i>Tribal Elder<br>Safety Network</div>
    </div>
    <h2>Do these stories<br>sound familiar to you?</h2>
    <ul>
      <li>My mother gets lost driving home from the store.</li>
      <li>I need help getting groceries and with chores at home.</li>
      <li>My dad wants to sleep all the time; he doesn't go out with friends anymore. He stopped drumming.</li>
      <li>My sister is raising 3 grandchildren on her own.</li>
      <li>My son is disrespecting me. He only comes to visit when my retirement money arrives. He always asks for money.</li>
    </ul>
    <div class="photo stories__photo" style="background:linear-gradient(180deg,rgba(255,255,255,0),#c9a486 30%,#7d5a4e 75%),linear-gradient(90deg,#4d6f93 0%,#8a4f4c 60%,rgba(241,226,226,0) 100%)" role="img" aria-label="Smiling older Native American couple standing outdoors in the desert"></div>
  </div>

  <div class="panel elders">
    <div class="resources__head">
      <div class="resources__figure" role="img" aria-label="Icon of an elderly man and woman with canes"></div>
      <div class="resources__title cond"><small>Resources for</small><big>Elders</big></div>
    </div>
    <div class="list">
      <div class="item">
        <svg width="14" height="14" viewBox="0 0 14 14"><circle cx="7" cy="7" r="6" fill="none" stroke="var(--rust)"/><path d="M4 7l2.2 2.3L12 2.5" fill="none" stroke="var(--rust)" stroke-width="1.3"/></svg>
        <div><h4>Elder Care Finder</h4>https://eldercarefinder.example/home<br>Call or Text: 1-800-555-0116<br>Email: help@eldercarefinder.example<br><em>For help finding support. Ask about services to Tribal Elders.</em></div>
      </div>
      <div class="item">
        <svg width="14" height="14" viewBox="0 0 14 14"><circle cx="7" cy="7" r="6" fill="none" stroke="var(--rust)"/><path d="M4 7l2.2 2.3L12 2.5" fill="none" stroke="var(--rust)" stroke-width="1.3"/></svg>
        <div><h4>National Memory Care Line</h4>(24 hours 7 days a week)<br>Call 1-800-555-0190<br><em>For support for people living with dementia, caregivers, families and the public. Connect with a live person who can provide information, local resources, crisis assistance and emotional support.</em></div>
      </div>
      <div class="item">
        <svg width="14" height="14" viewBox="0 0 14 14"><circle cx="7" cy="7" r="6" fill="none" stroke="var(--rust)"/><path d="M4 7l2.2 2.3L12 2.5" fill="none" stroke="var(--rust)" stroke-width="1.3"/></svg>
        <div><h4>Crisis &amp; Wellness Lifeline</h4>For mental health support, call 1-800-555-0988.</div>
      </div>
      <div class="item">
        <svg width="14" height="14" viewBox="0 0 14 14"><circle cx="7" cy="7" r="6" fill="none" stroke="var(--rust)"/><path d="M4 7l2.2 2.3L12 2.5" fill="none" stroke="var(--rust)" stroke-width="1.3"/></svg>
        <div><h4>State &amp; Tribal Hotlines | Tribal Elder Safety Network</h4>To find local resources within your tribe or state that specialize in elder abuse, neglect or exploitation, visit:<br><span class="url">https://nativeelders.example/safety/state-tribal-hotlines/</span></div>
      </div>
      <div class="item">
        <svg width="14" height="14" viewBox="0 0 14 14"><circle cx="7" cy="7" r="6" fill="none" stroke="var(--rust)"/><path d="M4 7l2.2 2.3L12 2.5" fill="none" stroke="var(--rust)" stroke-width="1.3"/></svg>
        <div><h4>Spirit Path Native Helpline</h4>A 24/7 safe, confidential and anonymous domestic and sexual violence helpline for Native Americans and Alaska Natives.<br>Call 1-844-555-0143<br>(1-844-555-HELP)<br>https://spiritpathhelpline.example/</div>
      </div>
    </div>
    <svg class="waves" width="220" height="30" viewBox="0 0 220 30"><path d="M20 14 C90 2 160 6 240 28 C160 14 90 14 20 14z" fill="var(--rust)"/></svg>
  </div>

  <div class="panel carers">
    <div class="resources__head">
      <div class="resources__figure" role="img" aria-label="Icon of a caregiver in scrubs with a stethoscope"></div>
      <div class="resources__title cond"><small>Resources for</small><big>Caregivers</big></div>
    </div>
    <div class="sub">Caring for an Older Adult</div>
    <div class="list">
      <div class="item">
        <svg width="14" height="14" viewBox="0 0 14 14"><circle cx="7" cy="7" r="6" fill="none" stroke="var(--teal-dark)"/><path d="M4 7l2.2 2.3L12 2.5" fill="none" stroke="var(--teal-dark)" stroke-width="1.3"/></svg>
        <div><h4>Elder Care Finder</h4>https://eldercarefinder.example/home<br>Call or Text: 1-800-555-0116<br>Email: help@eldercarefinder.example<br><em>For help finding support. Ask about services to Tribal Elders.</em></div>
      </div>
      <div class="item" style="border-bottom:none;margin-bottom:0">
        <svg width="14" height="14" viewBox="0 0 14 14"><circle cx="7" cy="7" r="6" fill="none" stroke="var(--teal-dark)"/><path d="M4 7l2.2 2.3L12 2.5" fill="none" stroke="var(--teal-dark)" stroke-width="1.3"/></svg>
        <div><h4>Memory Allies | Council for Native Elder Wellbeing</h4>An interactive educational program to better understand what dementia is and how it affects people.<br>https://nativeelders.example/memory-allies/</div>
      </div>
    </div>
    <div class="kin"><strong>Caring for a Grandchild</strong><span>Grandparents Raising Grandchildren<br>(Kinship Care)</span></div>
    <div class="list" style="padding-top:0">
      <div class="item">
        <svg width="14" height="14" viewBox="0 0 14 14"><circle cx="7" cy="7" r="6" fill="none" stroke="var(--teal-dark)"/><path d="M4 7l2.2 2.3L12 2.5" fill="none" stroke="var(--teal-dark)" stroke-width="1.3"/></svg>
        <div><h4>KinshipHomes.example</h4>An interactive website that seeks to share all relevant publicly available information impacting grandfamilies.</div>
      </div>
      <div class="item">
        <svg width="14" height="14" viewBox="0 0 14 14"><circle cx="7" cy="7" r="6" fill="none" stroke="var(--teal-dark)"/><path d="M4 7l2.2 2.3L12 2.5" fill="none" stroke="var(--teal-dark)" stroke-width="1.3"/></svg>
        <div><h4>Grandparent Resources | Tribal Elder Safety Network</h4>A list of resources for grandparents raising grandchildren.<br><span class="url">https://nativeelders.example/safety/grandparent-resources/</span></div>
      </div>
    </div>
    <svg class="waves" width="220" height="40" viewBox="0 0 220 40"><path d="M-10 14 C40 0 80 30 140 22 C180 16 200 6 220 4 V22 C190 26 170 36 120 36 C70 36 40 20 -10 14z" fill="var(--teal)"/></svg>
  </div>
</section>

</body>
</html>
```